House Church design model for faith-based organization

A design is needed for a house church model (Christian, faith-based). I’m looking for a graphic to convey four house church hallmarks showing the balance of member engagement. The four-part model includes - God’s Presence, Community, Discipleship, Outreach. The model should consist of the text for the four parts and the words - House Church

Perhaps a circular/modular design with House Church in the center. Using equally-sized interlocking slices or winged parts (graphically speaking, but not angelic wings) may help convey a balanced approach. It isn’t a process and should not appear in progressive steps, but the order (as listed) is used when explaining the concept. The model will be used for members to evaluate monthly focus.

I’m open to interpretation of the design and artwork. Designers should not feel a need to utilize cliché-like Christian symbols. However, if done minimally (and perhaps first century-like), they could be of interest (but are not required). Keeping it abstract may help readability and convey a roots/back-to-basics feel.

The artwork will be used for a video and PowerPoint presentation. It should be vector-based for simple movement/animation.

Additional thoughts:
Readable, not complex
Interesting interlocking design found at: https://www.plorvexia.com/circle-element-infographic-options-parts-steps-template-cycle-diagram-graph-round-chart-image572914386

Target Market(s)

To existing members (for reflection) and for those seeking a simpler church experience.

Requirements
Must have
• Simple, readable design, ability to reproduce for PowerPoint, video, and web. Prefer simple illustrations rather than images.
Nice to have
• The design should create a calming sense of focus on four priorities vs. the complexity of structure/requirements often found in the church experience.
Should not have
• Not crazy about puzzle pieces. Please avoid using all CAPS and serif fonts. Should not use complex images or photos.

```html
<!DOCTYPE html>
<html lang="en">
<head>
<meta charset="utf-8">
<title>House Church Model</title>
<link rel="stylesheet" href="https://fonts.googleapis.com/css2?family=Archivo+Black&display=swap">
<style>
  :root {
    --discipleship: #f07335;
    --outreach: #dfb505;
    --community: #1cc5d6;
    --presence: #b416dc;
    --hub-ink: #11395f;
    --label-ink: #ffffff;
    --paper: #ffffff;
  }
  html, body {
    margin: 0;
    padding: 0;
    width: 1200px;
    height: 1196px;
    overflow: hidden;
    background: var(--paper);
  }
  .model {
    display: block;
    width: 1200px;
    height: 1196px;
  }
  .petal-ring {
    fill: none;
    stroke-width: 50;
    stroke-linecap: round;
  }
  .petal-body { stroke: none; }
  .hub { fill: var(--paper); }
  .label {
    font-family: "Archivo Black", "Arial Black", sans-serif;
    fill: var(--label-ink);
    font-size: 44px;
    text-anchor: middle;
  }
  .hub-label {
    font-family: "Archivo Black", "Arial Black", sans-serif;
    fill: var(--hub-ink);
    font-size: 54px;
    text-anchor: middle;
  }
  .discipleship { --tone: var(--discipleship); }
  .outreach { --tone: var(--outreach); }
  .community { --tone: var(--community); }
  .presence { --tone: var(--presence); }
  .petal .petal-ring { stroke: var(--tone); }
  .petal .petal-body { fill: var(--tone); }
</style>
</head>
<body>
<svg class="model" viewBox="0 0 1326 1322" xmlns="http://www.w3.org/2000/svg" role="img" aria-label="House Church model: God's Presence, Community, Discipleship, Outreach">
  <defs>
    <g id="petal-shape">
      <path class="petal-ring" d="M 423 410 A 249 249 0 1 1 911 395"/>
      <path class="petal-body" d="M 498 468 A 200 200 0 1 1 828 468 L 735 520 L 663 600 L 590 520 Z"/>
    </g>
  </defs>

  <g class="petal presence" transform="rotate(-90 663 648)"><use href="#petal-shape"/></g>
  <g class="petal community" transform="rotate(180 663 648)"><use href="#petal-shape"/></g>
  <g class="petal outreach" transform="rotate(90 663 648)"><use href="#petal-shape"/></g>
  <g class="petal discipleship"><use href="#petal-shape"/></g>

  <circle class="hub" cx="661" cy="630" r="135"/>

  <text class="label" x="664" y="335">Discipleship</text>
  <text class="label" x="975" y="662">Outreach</text>
  <text class="label" x="662" y="970">Community</text>
  <text class="label" x="370" y="640">God's</text>
  <text class="label" x="370" y="690">Presence</text>

  <text class="hub-label" x="661" y="620">House</text>
  <text class="hub-label" x="661" y="678">Church</text>
</svg>
</body>
</html>
```